Easy - Design our new Brochure for our door to door team.

We need a new corporate/high end home services brochure for our new door to door sales team.
This Job will likely need the same designer for other content and marketing collateral that we need designed as part of this project.
We have just merged 2 companies and we would like that to be considered in the design of the brochure, using the merger as a selling point, so we would like the 2 companies logos to be used together in a creative way to signify that "BrightHaven Property Services" have merged with "Manor Rinse Pros" and as you'll hopefully understand we have a big focus on both the companies being the best in our industry in Australia.
We have put together a package we will be selling, using this brochure as our sales tool document. So we are looking for something innovative, stylish and should focus on peoples homes and their families.
The parts of the brochure that talk about the dangers of mould will need to have clever design and imagery to remind the home owner about the dangers of mould around the home.
The details of whats included in the package "Section" need to look well presented with a list of the services looking stylish, neat, easy to understand and see the value in.
We would like designers to use the simple example mock up we have provided as a draft for content placement guide and to really take creative control and show us how great you'd design the brochure.
The brochure will be a tri-fold brochure and the inside left and middle panels will have the information and package items listed for the customer to keep until the service day. The far right inside panel will be an information section that needs to look secure and simple, and safe as our team will be taking payment at the door and holding on to the far right panel that will have a perforated line cut into the card board package certificate.
On the details section, each brochure we have printed will have an individual certificate number. This number will be on the part that the customer keeps and the part that we keep. The area for the number can stay blank as we will have to organise this at print stage unless you have a suggestion for that.
This brochure will be printed on thick card at high resolution so attention to detail is important. As long as the logo colours are used we want to see it done well.
There is a section on the back that says back of the customer details form about The Reward Pocket App(tm) promotion. Please leave this blank for the moment and we will work with a designer on this section separately. Please look at both of our websites when designing the brochure.
www.manorrinsepros.com.au
www.brighthaven.net.au
Below I have put all the text content. This can be modified to an extent for the design, but needs to have all the content. Because there is a reasonable amount of text please try and make the brochure flow and not look crowded.
We are excited to see what gets put together.
Thank you

```html
<!DOCTYPE html>
<html lang="en">
<head>
<meta charset="UTF-8">
<title>BrightHaven Property Services – Promotional Package Brochure</title>
<link rel="stylesheet" href="https://fonts.googleapis.com/css2?family=Open+Sans:wght@300;400;600;700&display=swap">
<style>
  :root {
    --sky-top: #a9d2ef;
    --sky-fade: #ffffff;
    --peach: #fde3c6;
    --orange: #f7941d;
    --blue: #1f72b8;
    --red: #e8392f;
    --ink: #2b2b2b;
    --body: #5a5a5a;
    --muted: #8a8a8a;
    --rule: #e4e4e4;
    --field-border: #cfcfcf;
    --soft-blue: #dcedf8;
    --soft-peach: #fde6cf;
  }
  * { box-sizing: border-box; margin: 0; padding: 0; }
  html, body { width: 1200px; height: 848px; overflow: hidden; }
  body {
    font-family: "Open Sans", Arial, sans-serif;
    color: var(--body);
    background: #fff;
  }
  .brochure {
    position: relative;
    width: 1200px;
    height: 848px;
    background: linear-gradient(to bottom, var(--sky-top) 0%, #e4f1fa 14%, var(--sky-fade) 30%, var(--sky-fade) 82%, var(--peach) 100%);
    overflow: hidden;
  }
  .panel-rule {
    position: absolute;
    top: 50px;
    width: 1px;
    height: 760px;
    background: var(--rule);
  }
  .panel-rule--one { left: 405px; }
  .panel-rule--two { left: 796px; }

  /* Left panel */
  .brand-pair {
    position: absolute;
    left: 20px;
    top: 112px;
    display: flex;
    align-items: center;
    gap: 36px;
  }
  .brand-name {
    display: flex;
    align-items: center;
    gap: 7px;
    font-weight: 700;
    font-size: 17px;
    color: var(--ink);
    line-height: 1;
  }
  .brand-name--washing { color: var(--blue); font-size: 15px; }
  .brand-dot { width: 14px; height: 14px; border-radius: 50%; background: var(--orange); }
  .brand-square { width: 13px; height: 13px; background: var(--blue); }

  .intro-copy {
    position: absolute;
    left: 13px;
    top: 180px;
    width: 380px;
  }
  .intro-copy p {
    font-size: 12.2px;
    line-height: 17.3px;
    text-align: justify;
    margin-bottom: 17px;
  }

  /* Warning box */
  .warning {
    position: absolute;
    left: 9px;
    top: 608px;
    width: 780px;
    height: 224px;
    background: linear-gradient(to bottom, #ffffff 0%, #fff7ef 100%);
    box-shadow: 0 0 10px rgba(232, 57, 47, 0.22);
  }
  .warning-title {
    position: absolute;
    left: 13px;
    top: 6px;
    font-weight: 400;
    line-height: 1.05;
  }
  .warning-title .alert { display: block; font-size: 30px; color: var(--red); }
  .warning-title .topic { display: block; font-size: 29px; font-weight: 300; color: var(--blue); }
  .warning-columns {
    position: absolute;
    left: 13px;
    top: 84px;
    width: 756px;
    column-count: 2;
    column-gap: 26px;
    height: 110px;
  }
  .warning-columns p {
    font-size: 12.2px;
    line-height: 17.3px;
    text-align: justify;
    color: var(--muted);
    margin-bottom: 17px;
  }

  /* Middle panel */
  .package-heading {
    position: absolute;
    left: 426px;
    top: 46px;
    line-height: 1.2;
  }
  .package-heading .lead { display: block; font-size: 30px; font-weight: 300; color: var(--ink); }
  .package-heading .title { display: block; font-size: 30px; font-weight: 600; color: var(--orange); letter-spacing: 0.3px; }

  .package-list {
    position: absolute;
    left: 426px;
    top: 204px;
    width: 355px;
    list-style: none;
  }
  .package-list li {
    position: relative;
    padding-left: 32px;
    font-size: 12.2px;
    line-height: 17px;
    color: var(--ink);
    text-align: justify;
  }
  .package-list li::before {
    content: "";
    position: absolute;
    left: 0;
    top: 2px;
    width: 18px;
    height: 18px;
    border-radius: 50%;
    background: var(--orange);
  }
  .package-list li:nth-child(1) { height: 57px; }
  .package-list li:nth-child(2) { height: 57px; }
  .package-list li:nth-child(3) { height: 57px; }

  .feature-card {
    position: absolute;
    left: 410px;
    width: 381px;
    height: 81px;
    background: #fff;
    border: 1px solid var(--rule);
    box-shadow: 0 1px 5px rgba(0,0,0,0.12);
    display: flex;
    align-items: center;
    gap: 14px;
    padding: 0 15px;
  }
  .feature-card--one { top: 417px; }
  .feature-card--two { top: 516px; }
  .feature-card p {
    font-size: 12.2px;
    line-height: 17px;
    color: var(--muted);
    text-align: justify;
    flex: 1;
  }
  .feature-mark { width: 62px; height: 62px; border-radius: 50%; flex: none; }
  .feature-mark--blue { background: var(--soft-blue); }
  .feature-mark--peach { background: var(--soft-peach); }

  /* Right panel */
  .certificate-brand {
    position: absolute;
    left: 828px;
    top: 118px;
    display: flex;
    align-items: center;
    gap: 12px;
    color: var(--ink);
    font-weight: 700;
  }
  .certificate-brand .mark { width: 30px; height: 30px; border-radius: 50%; background: var(--orange); }
  .certificate-brand .name { font-size: 50px; line-height: 1; letter-spacing: -1px; }
  .certificate-brand .tagline { display: block; font-size: 14px; letter-spacing: 4.6px; margin-top: 6px; text-align: right; }

  .details-form {
    position: absolute;
    left: 809px;
    top: 232px;
    width: 381px;
    list-style: none;
  }
  .details-form li {
    height: 40px;
    margin-bottom: 2.8px;
    border: 1px solid var(--field-border);
    background: #fff;
    padding-left: 8px;
    font-size: 15px;
    line-height: 38px;
    color: var(--body);
  }
  .cert-number {
    position: absolute;
    left: 817px;
    top: 489px;
    font-size: 19px;
    color: var(--body);
  }
  .offer {
    position: absolute;
    left: 800px;
    width: 400px;
    text-align: center;
    font-weight: 700;
    font-size: 34px;
    line-height: 1.25;
  }
  .offer--value { top: 558px; color: var(--blue); }
  .offer--price { top: 600px; color: var(--red); }
  .congrats {
    position: absolute;
    left: 800px;
    top: 702px;
    width: 400px;
    text-align: center;
    font-weight: 700;
    font-size: 29px;
    color: var(--orange);
  }
</style>
</head>
<body>
<main class="brochure">
  <span class="panel-rule panel-rule--one"></span>
  <span class="panel-rule panel-rule--two"></span>

  <!-- Inside left panel -->
  <section class="panel-intro">
    <div class="brand-pair">
      <span class="brand-name"><span class="brand-dot"></span>BrightHaven</span>
      <span class="brand-name brand-name--washing"><span class="brand-square"></span>Manor Rinse Pros</span>
    </div>
    <div class="intro-copy">
      <p>Lorem ipsum dolor sit amet, consectetur adipisicing elit, sed do eiusmod tempor incididunt ut labore et dolore magna aliqua. Ut enim ad minim veniam, quis nostrud exercitation ullamco laboris nisi ut aliquip ex ea commodo consequat. Duis aute irure dolor in reprehenderit in voluptate velit esse cillum dolore eu fugiat nulla pariatur. Excepteur sint occaecat cupidatat non proident, sunt in culpa qui officia deserunt mollit anim id est laborum.</p>
      <p>Lorem ipsum dolor sit amet, consectetur adipisicing elit, sed do eiusmod tempor incididunt ut labore et dolore magna aliqua. Ut enim ad minim veniam, quis nostrud exercitation ullamco laboris nisi ut aliquip ex ea commodo consequat. Duis aute irure dolor in reprehenderit in voluptate velit esse cillum dolore eu fugiat nulla pariatur. Excepteur sint occaecat cupidatat non proident, sunt in culpa qui officia deserunt mollit anim id est laborum.</p>
      <p>Lorem ipsum dolor sit amet, consectetur adipisicing elit, sed do eiusmod tempor incididunt ut labore et dolore magna aliqua. Ut enim ad minim veniam, quis nostrud exercitation ullamco laboris nisi ut aliquip ex ea commodo consequat. Duis aute irure dolor in reprehenderit in voluptate velit esse cillum dolore eu fugiat nulla pariatur. Excepteur sint occaecat cupidatat non proident, sunt in culpa qui officia deserunt mollit anim id est laborum.</p>
    </div>
  </section>

  <!-- Inside middle panel -->
  <section class="panel-package">
    <h2 class="package-heading">
      <span class="lead">Our Special</span>
      <span class="title">PROMOTIONAL PACKAGE</span>
    </h2>
    <ul class="package-list">
      <li>Lorem ipsum dolor sit amet, consectetur adipisicing elit, sed do eiusmod tempor</li>
      <li>Lorem ipsum dolor sit amet, consectetur</li>
      <li>Lorem ipsum dolor sit amet, consectetur adipisicing elit, sed do eiusmod tempor</li>
      <li>Lorem ipsum dolor sit amet, consectetur</li>
    </ul>
    <div class="feature-card feature-card--one">
      <p>Lorem ipsum dolor sit amet, consectetur adipisicing elit, sed do eiusmod tempor incidi-</p>
      <span class="feature-mark feature-mark--blue"></span>
    </div>
    <div class="feature-card feature-card--two">
      <span class="feature-mark feature-mark--peach"></span>
      <p>Lorem ipsum dolor sit amet, consectetur adipisicing elit, sed do eiusmod tempor incidi-</p>
    </div>
  </section>

  <!-- Mould warning spanning left and middle -->
  <section class="warning">
    <h2 class="warning-title">
      <span class="alert">WARNING</span>
      <span class="topic">Mold Health &amp; Safety</span>
    </h2>
    <div class="warning-columns">
      <p>Lorem ipsum dolor sit amet, consectetur adipisicing elit, sed do eiusmod tempor incididunt ut labore et dolore magna aliqua. Ut enim ad minim veniam, quis nostrud exercitation ullamco laboris nisi ut aliquip ex ea commodo consequat. Duis aute irure dolor in reprehenderit in voluptate velit esse cillum dolore eu fugiat nulla pariatur. Excepteur sint occaecat cupidatat non proident, sunt in culpa qui officia deserunt mollit anim id est laborum.</p>
      <p>Lorem ipsum dolor sit amet, consectetur adipisicing elit, sed do eiusmod tempor incididunt ut labore et dolore magna aliqua. Ut enim ad minim veniam, quis nostrud exercitation ullamco</p>
    </div>
  </section>

  <!-- Inside right panel: customer certificate -->
  <section class="panel-certificate">
    <div class="certificate-brand">
      <span class="mark"></span>
      <div>
        <span class="name">BrightHaven</span>
        <span class="tagline">PROPERTY SERVICES</span>
      </div>
    </div>
    <ul class="details-form">
      <li>Name:</li>
      <li>Phone:</li>
      <li>Email:</li>
      <li>Address:</li>
      <li>Address:</li>
      <li>Date:</li>
    </ul>
    <p class="cert-number">CERT NO:&nbsp; 2063</p>
    <p class="offer offer--value">WORTH OVER $750</p>
    <p class="offer offer--price">ONLY $299 TODAY</p>
    <p class="congrats">CONGRADULATIONS !</p>
  </section>
</main>
</body>
</html>
```